TRNV LLP website - revamping our website after 23 years

Our website needs a complete overhaul. The purpose of this exercise is to provide us with your vision of what you think the website should look like. We don't need the website to be created or coded. Just need creative designs.

We have a four sites that we would like to base our website on;

We like the simplicity of Fairwicks, the style of Pemberly Strand and Kettridge.

http://www.pemberlystrand-example.com/en/toronto-ontario/
http://www.fairwicks-example.ca/
hallkettridge-example.com
http://www.vendrupe-example.com/our-professionals.html

We have a logo that we would like to use which will be attached below. We need to keep our website looking very professional as we have a large number of high net worth clients.
Updates

Hi, We've received some good website designs but they appear to be the same type of template websites we've received in the past - this is not what we're looking for. What we want is a unique website that is modelled on the following three company websites: http://www.fairwicks-example.ca/ www.hallkettridge-example.com/ http://www.pemberlystrand-example.com/en/toronto-ontario/

Thank you everyone for your designs. I will be posting updates and my comments on the various designs in the next day - I want to thank you for the creative designs I see. I thought i would explain a bit about our firm and perhaps it can help when you design the theme of our website: - Our firm is like a family and our clients are truly like our friends. We have close knit relationships in and outside of the office with staff and clients. - We are an 'out of the box' type of firm. We operate differently than most firms and that's a differentiating factor in what makes us who we are - Our slogan is "Count on us" which is a testament to the way we run our practice - We would like an open, fresh, clean look to our website - we don't want the landing page to be overly long or complex because we have limited time to update the website and limited content That's it for the time being - when things come to mind I will post them here.

Can we try a design as follows: - make the website look very similar to www.fairwicks-example.ca - use the same background colour - Keep the same black top but insert our logo - incorporate some of the content from our current website www.trnv-example.com

I have been away dealing with a personal matter. I will look into these websites tomorrow afternoon and provide more feedback / info on the top designer. Thank you

Hi designers, I want to apologize for the delay. I plan on wrapping things up within the next few days. I will go through a few of the top designs and offer my comments. Thank you for your patience.

Target Market(s)

Mainly our current clients - We have a large number of high net worth individuals as clients.

Industry/Entity Type

Accounting

Number of Pages Required

1 page

Requirements
Must have
• Please model website on the websites indicated above.
• Our current website is www.trnv-example.com. It's dark, cluttered and not inviting. We want a fresh, clean website. Please incorporate the logo's attached below.

```html
<!DOCTYPE html>
<html lang="en">
<head>
<meta charset="utf-8">
<title>TRNV LLP — Chartered Professional Accountants</title>
<link rel="stylesheet" href="https://fonts.googleapis.com/css2?family=Rokkitt:wght@400;500;600&family=Lato:wght@400;700&display=swap">
<style>
:root{
  --ink:#2b2b2b;
  --muted:#6b6b6b;
  --bar:#333335;
  --header:#f3f3f3;
  --blue:#2aa3de;
  --plum:#a3195b;
  --green:#8cc63f;
  --sky:#2aaae2;
  --violet:#6a2c91;
  --footer:#3a3a3c;
  --footer-text:#a9a9a9;
  --card:#f2f2f2;
  --white:#ffffff;
}
*{box-sizing:border-box;margin:0;padding:0}
html,body{width:693px;height:1200px;overflow:hidden;background:var(--white)}
body{position:relative;font-family:"Lato",Arial,sans-serif;color:var(--ink)}
.abs{position:absolute}
.serif{font-family:"Rokkitt",Georgia,serif}

/* top bar */
.topbar{left:0;top:0;width:693px;height:19px;background:var(--bar);color:#ddd;font-size:8px;font-family:"Rokkitt",Georgia,serif}
.topbar .welcome{left:42px;top:4px}
.topbar .links{right:68px;top:4px;word-spacing:6px}
.topbar .social{right:44px;top:6px;display:flex;gap:5px}
.topbar .social span{width:7px;height:7px;border-radius:50%;background:#aaa;display:block}

/* header */
.header{left:0;top:19px;width:693px;height:111px;background:var(--header)}
.header-rule{left:0;top:130px;width:693px;height:3px;background:var(--blue)}
.brand{left:44px;top:62px;display:flex;align-items:center;gap:7px}
.brand .mark{width:16px;height:16px;background:var(--plum)}
.brand .name{font-family:"Rokkitt",Georgia,serif;font-size:24px;color:#3b3b3b;letter-spacing:.5px}
.brand-sub{left:44px;top:91px;font-size:5px;letter-spacing:.6px;color:#777;font-family:"Rokkitt",Georgia,serif}
.slogan{left:244px;top:52px;font-family:"Rokkitt",Georgia,serif;font-size:13px;color:var(--plum)}
.info{top:35px;font-family:"Rokkitt",Georgia,serif;font-size:8.5px;color:#555;line-height:1.45}
.info svg{display:block;margin-bottom:6px}
.info b{font-weight:500;color:#222}
.info-sep{top:40px;width:1px;height:44px;background:#dcdcdc}
.nav{left:222px;top:105px;display:flex;font-family:"Rokkitt",Georgia,serif;font-size:9.5px;color:#333}
.nav a{display:block;height:25px;line-height:26px;padding:0 10.5px;text-decoration:none;color:inherit}
.nav a.active{background:var(--blue);color:#fff;padding:0 12.5px}

/* hero */
.hero{left:0;top:133px;width:693px;height:309px;background:linear-gradient(90deg,#bfc6cc 0%,#d8c6b4 25%,#e2d6c9 50%,#b9b4b2 75%,#8d8f96 100%)}
.hero-kicker{left:322px;top:284px;font-family:"Rokkitt",Georgia,serif;font-size:10px;color:#222}
.hero-title{left:322px;top:293px;font-family:"Rokkitt",Georgia,serif;font-weight:600;font-size:23px;color:#1d1d1d;white-space:nowrap}
.hero-title .hl{color:var(--plum)}
.hero-title .num{font-style:italic;font-size:29px}
.hero-sub{left:412px;top:323px;font-family:"Rokkitt",Georgia,serif;font-size:10px;color:#222}
.slider-tab{left:308px;top:422px;width:76px;height:20px;background:#fff;border-radius:12px 12px 0 0}
.slider-dots{left:325px;top:430px;display:flex;gap:3px}
.slider-dots span{width:7px;height:7px;border-radius:50%;background:#ddd;display:block}
.slider-dots span.on{background:var(--blue)}

/* welcome card */
.welcome-card{left:42px;top:476px;width:192px;height:391px;background:var(--card)}
.welcome-photo{left:42px;top:476px;width:192px;height:114px;background:linear-gradient(135deg,#6c7b86,#a08478 55%,#cfd6dc)}
.welcome-title{left:53px;top:597px;font-family:"Rokkitt",Georgia,serif;font-size:15.5px;color:#222}
.welcome-text{left:53px;top:617px;width:175px;font-size:7.7px;line-height:15px;color:#666}
.btn-more{left:53px;top:834px;width:66px;height:22px;background:#2d2d2d;color:#fff;font-family:"Rokkitt",Georgia,serif;font-size:8px;text-align:center;line-height:22px;border-radius:2px}

/* services */
.diff-title{left:262px;top:472px;font-family:"Rokkitt",Georgia,serif;font-size:14.5px;color:#222}
.diff-sub{left:262px;top:493px;font-family:"Rokkitt",Georgia,serif;font-size:8.3px;color:#333}
.service{width:200px;display:flex;gap:10px}
.service svg{flex:none}
.service h3{font-family:"Rokkitt",Georgia,serif;font-weight:400;font-size:9.5px;color:var(--blue);margin-bottom:6px}
.service p{font-size:7.4px;line-height:11.5px;color:#777}

/* calls to action */
.cta{top:900px;width:140px;height:72px;background:#fff;text-align:center;font-family:"Rokkitt",Georgia,serif}
.cta .top{height:48px;color:#fff;padding-top:10px}
.cta .top strong{display:block;font-weight:500;font-size:14.5px;line-height:1}
.cta .top span{display:block;font-size:8.5px;margin-top:4px}
.cta .go{height:20px;line-height:21px;font-size:8px;color:#333;border-left:1px solid #e6e6e6;border-right:1px solid #e6e6e6}
.cta .bottom{height:4px}
.cta.plum .top,.cta.plum .bottom{background:var(--plum)}
.cta.green .top,.cta.green .bottom{background:var(--green)}
.cta.sky .top,.cta.sky .bottom{background:var(--sky)}
.cta.violet .top,.cta.violet .bottom{background:var(--violet)}

/* footer */
.footer{left:0;top:1004px;width:693px;height:196px;background:var(--footer);color:var(--footer-text)}
.f-head{top:1028px;font-family:"Rokkitt",Georgia,serif;font-size:10px;color:#fff}
.news{left:42px;width:110px;font-size:7px;line-height:9.5px;color:#b5b5b5}
.news small{display:block;font-size:5.5px;color:#8a8a8a}
.jobs{top:1047px;font-size:7px;line-height:16px;color:#a9a9a9}
.nl-text{left:458px;top:1046px;width:200px;font-size:7px;line-height:14px;color:#a9a9a9}
.field{left:458px;width:128px;height:21px;background:#f5f5f5;border-radius:3px;font-size:7.5px;color:#666;display:flex;align-items:center;gap:5px;padding-left:6px}
.signup{left:592px;top:1082px;width:58px;height:48px;background:var(--blue);border-radius:3px;color:#fff;text-align:center;font-family:"Rokkitt",Georgia,serif;font-size:10px}
.signup svg{display:block;margin:8px auto 3px}
.f-bottom{left:42px;top:1178px;font-size:7px;color:#9a9a9a}
.f-follow{right:44px;top:1178px;font-size:7px;color:#9a9a9a;display:flex;gap:6px;align-items:center}
.f-follow i{width:6px;height:6px;border-radius:50%;background:#888;display:block}
</style>
</head>
<body>

<!-- top bar -->
<div class="abs topbar">
  <div class="abs welcome">Welcome to TRNV LLP, - 18 December 2015</div>
  <div class="abs links">News Site&nbsp;Map</div>
  <div class="abs social"><span></span><span></span><span></span></div>
</div>

<!-- header -->
<header class="abs header"></header>
<div class="abs brand"><span class="mark"></span><span class="name">TRNV LLP</span></div>
<div class="abs brand-sub">CHARTERED PROFESSIONAL ACCOUNTANTS</div>
<div class="abs slogan">Count on us !</div>

<div class="abs info" style="left:362px">
  <svg width="18" height="18" viewBox="0 0 18 18" fill="none" stroke="#2aa3de" stroke-width="1.2"><circle cx="9" cy="9" r="7.5"/><path d="M9 4.5V9l3 2"/></svg>
  Hours of Operation :<br><b>9:00am to 5:00pm</b>
</div>
<div class="abs info-sep" style="left:460px"></div>
<div class="abs info" style="left:482px">
  <svg width="18" height="18" viewBox="0 0 18 18" fill="none" stroke="#2aa3de" stroke-width="1.2"><path d="M4 2.5l3 3-1.5 2a9 9 0 0 0 5 5l2-1.5 3 3-2 2C7 15 3 11 2 4.5z"/></svg>
  Call Us Today!<br><b>(416) 555-0142</b>
</div>
<div class="abs info-sep" style="left:563px"></div>
<div class="abs info" style="left:580px">
  <svg width="18" height="18" viewBox="0 0 18 18" fill="none" stroke="#2aa3de" stroke-width="1.2"><rect x="1.5" y="4" width="15" height="11"/><path d="M1.5 4l7.5 6 7.5-6"/></svg>
  Email Us :<br><b>info@trnv-example.com</b>
</div>

<nav class="abs nav">
  <a class="active">HOME</a><a>ABOUT TRNV</a><a>SERVICES</a><a>LIBRARY</a><a>LINKS</a><a>CAREERS</a><a>CONTACT US</a>
</nav>
<div class="abs header-rule"></div>

<!-- hero -->
<div class="abs hero" role="img" aria-label="Photo of a smiling professional in a suit with colleagues blurred behind him"></div>
<div class="abs hero-kicker">Together,</div>
<div class="abs hero-title">WE BRING OVER <span class="hl num">100</span> <span class="hl">YEARS</span> OF</div>
<div class="abs hero-sub">Valuable Experience to the pratice of public accounting</div>
<div class="abs slider-tab"></div>
<div class="abs slider-dots"><span class="on"></span><span></span><span></span><span></span><span></span></div>

<!-- welcome -->
<div class="abs welcome-card"></div>
<div class="abs welcome-photo" role="img" aria-label="Photo of a team meeting around a boardroom table"></div>
<h2 class="abs welcome-title" style="font-weight:400">Welcome to TRNV LLP</h2>
<p class="abs welcome-text">TRNV, Thornvale Rennick Norwood Vale LLP Chartered Accountants, is a full-service, public accounting firm, primarily serving the small and mid-size, entrepreneurial business and professional sectors in Toronto Canada. TRNV's experienced partners and professional, support staff strive to provide accounting and advisory services using an invaluable personal approach, designed to meet each client's individual needs. This “personal touch”, combined with a full range of accounting, auditing, tax compliance and planning services allows TRNV to meet all your business and personal accounting requirements.</p>
<div class="abs btn-more">LEARN MORE</div>

<!-- services -->
<h2 class="abs diff-title" style="font-weight:400">Why We are Different</h2>
<p class="abs diff-sub">These services can be obtained from the descriptions contained in the Services Section</p>

<div class="abs service" style="left:262px;top:518px">
  <svg width="34" height="30" viewBox="0 0 34 30" fill="none" stroke="#2aa3de" stroke-width="1.3"><rect x="1" y="2" width="20" height="24"/><path d="M5 8h12M5 13h12M5 18h8"/><circle cx="25" cy="19" r="6"/><path d="M29 23l4 5"/></svg>
  <div><h3>Accounting &amp; Auditing</h3><p>Sed diam nonummy nibh euismod tincidunt as ut. Ut wisi enim ...</p></div>
</div>
<div class="abs service" style="left:470px;top:518px">
  <svg width="32" height="30" viewBox="0 0 32 30" fill="none" stroke="#2aa3de" stroke-width="1.3"><rect x="4" y="2" width="22" height="18"/><path d="M8 16l5-5 4 3 6-7M10 20l-3 9M20 20l3 9"/></svg>
  <div><h3>Business Advisory</h3><p>Sed diam nonummy nibh euismod tincidunt as ut. Ut wisi enim ...</p></div>
</div>
<div class="abs service" style="left:262px;top:580px">
  <svg width="34" height="30" viewBox="0 0 34 30" fill="none" stroke="#2aa3de" stroke-width="1.3"><rect x="9" y="1" width="22" height="26"/><path d="M14 7h12M20 12h6M20 17h6"/><circle cx="11" cy="16" r="6"/><path d="M7 20l-5 6"/></svg>
  <div><h3>Due Diligence</h3><p>Sed diam nonummy nibh euismod tincidunt as ut. Ut wisi enim ...</p></div>
</div>
<div class="abs service" style="left:468px;top:580px">
  <svg width="34" height="30" viewBox="0 0 34 30" fill="none" stroke="#2aa3de" stroke-width="1.3"><rect x="2" y="3" width="9" height="7"/><rect x="23" y="3" width="9" height="7"/><circle cx="17" cy="12" r="4"/><path d="M9 28v-6a8 8 0 0 1 16 0v6M2 28h30"/></svg>
  <div><h3>High-Tech Industry</h3><p>Sed diam nonummy nibh euismod tincidunt as ut. Ut wisi enim ...</p></div>
</div>
<div class="abs service" style="left:262px;top:642px">
  <svg width="30" height="30" viewBox="0 0 30 30" fill="none" stroke="#2aa3de" stroke-width="1.3"><rect x="9" y="1" width="12" height="10" rx="2"/><path d="M15 3v6M12 6h6M4 29v-7a7 7 0 0 1 7-7h8a7 7 0 0 1 7 7v7z"/></svg>
  <div><h3>Medical Professionals</h3><p>Sed diam nonummy nibh euismod tincidunt as ut. Ut wisi enim ...</p></div>
</div>
<div class="abs service" style="left:470px;top:642px">
  <svg width="30" height="30" viewBox="0 0 30 30" fill="none" stroke="#2aa3de" stroke-width="1.3"><path d="M3 2h16l4 4v20H3z"/><path d="M7 9h10M7 14h6"/><circle cx="22" cy="22" r="6"/><path d="M19 25l6-6"/></svg>
  <div><h3>Personal Tax Services</h3><p>Sed diam nonummy nibh euismod tincidunt as ut. Ut wisi enim ...</p></div>
</div>
<div class="abs service" style="left:262px;top:704px">
  <svg width="34" height="30" viewBox="0 0 34 30" fill="none" stroke="#2aa3de" stroke-width="1.3"><path d="M2 5h10l3 3h17v20H2z"/><path d="M7 23l7-7 5 4 8-9M22 11h5v5"/></svg>
  <div><h3>Investors &amp;Wealth Management</h3><p>Sed diam nonummy nibh euismod tincidunt as ut. Ut wisi enim ...</p></div>
</div>
<div class="abs service" style="left:470px;top:704px">
  <svg width="32" height="30" viewBox="0 0 32 30" fill="none" stroke="#2aa3de" stroke-width="1.3"><rect x="3" y="2" width="12" height="26"/><rect x="15" y="12" width="14" height="16"/><path d="M6 6h6M6 11h6M6 16h6M6 21h6M19 17h6M19 22h6"/></svg>
  <div><h3>The Real Estate Industry</h3><p>Sed diam nonummy nibh euismod tincidunt as ut. Ut wisi enim ...</p></div>
</div>
<div class="abs service" style="left:262px;top:766px">
  <svg width="30" height="30" viewBox="0 0 30 30" fill="none" stroke="#2aa3de" stroke-width="1.3"><path d="M2 28h26M4 28v-8h5v8M12 28V14h5v14M20 28V9h5v19"/><circle cx="12" cy="6" r="4.5"/></svg>
  <div><h3>Not for Profit &amp; Charitable Sector</h3><p>Sed diam nonummy nibh euismod tincidunt as ut. Ut wisi enim ...</p></div>
</div>
<div class="abs service" style="left:468px;top:766px">
  <svg width="34" height="30" viewBox="0 0 34 30" fill="none" stroke="#2aa3de" stroke-width="1.3"><rect x="2" y="5" width="20" height="20"/><path d="M6 11h12M6 16h12M6 21h8"/><circle cx="25" cy="16" r="7"/><path d="M25 12v4h3"/></svg>
  <div><h3>The Legal Profession</h3><p>Sed diam nonummy nibh euismod tincidunt as ut. Ut wisi enim ...</p></div>
</div>
<div class="abs service" style="left:262px;top:828px">
  <svg width="26" height="30" viewBox="0 0 26 30" fill="none" stroke="#2aa3de" stroke-width="1.3"><circle cx="13" cy="15" r="11"/><path d="M13 4v11l8 7"/><path d="M13 15L4 10" /></svg>
  <div><h3>Tax Planning and Compliance</h3><p>Sed diam nonummy nibh euismod tincidunt as ut. Ut wisi enim ...</p></div>
</div>

<!-- calls to action -->
<div class="abs cta plum" style="left:42px"><div class="top"><strong>2015 Tax Estimator</strong><span>For 2014 Now Online!</span></div><div class="go">CLICK HERE TO BEGIN</div><div class="bottom"></div></div>
<div class="abs cta green" style="left:198px"><div class="top"><strong>Game of Tax</strong><span>Personal Tax Commentary 14-15</span></div><div class="go">CLICK HERE TO BEGIN</div><div class="bottom"></div></div>
<div class="abs cta sky" style="left:354px"><div class="top"><strong>TRNV Tax Tips</strong><span>Same Sex Couple</span></div><div class="go">CLICK HERE TO BEGIN</div><div class="bottom"></div></div>
<div class="abs cta violet" style="left:510px"><div class="top"><strong>FeedBack</strong><span>Fill the details &amp; Contact Me!.</span></div><div class="go">CLICK HERE TO BEGIN</div><div class="bottom"></div></div>

<!-- footer -->
<footer class="abs footer"></footer>
<div class="abs f-head" style="left:42px">Latest News</div>
<div class="abs news" style="top:1047px">Lorem ipsum dolor sit amet, consectetur adipiscing elit ...<small>September 16, 2015</small></div>
<div class="abs news" style="top:1083px">Lorem ipsum dolor sit amet, consectetur adipiscing elit ...<small>September 16, 2015</small></div>
<div class="abs news" style="top:1119px">Lorem ipsum dolor sit amet, consectetur adipiscing elit ...<small>September 16, 2015</small></div>

<div class="abs f-head" style="left:171px">Featured Careers / Jobs</div>
<div class="abs jobs" style="left:171px">Accounting and Auditing<br>Business Advisory<br>Due Diligence<br>High-Tech Industry<br>Investors and Wealth Management<br>Medical Professionals</div>
<div class="abs jobs" style="left:310px">Not for Profit and Charitable Sector<br>Personal Tax Services<br>The Legal Profession<br>The Real Estate Industry<br>Tax Planning and Compliance</div>

<div class="abs f-head" style="left:458px">Newsletter Sign Up - Today!!!</div>
<p class="abs nl-text">Enter your name and email to subscribe or unsubscribe to our newsletters and receive latest offers!!!..</p>
<div class="abs field" style="top:1082px"><svg width="8" height="8" viewBox="0 0 8 8" fill="#2aa3de"><circle cx="4" cy="2.2" r="2"/><path d="M0 8a4 3.5 0 0 1 8 0z"/></svg>Enter Your Name</div>
<div class="abs field" style="top:1109px"><svg width="8" height="8" viewBox="0 0 8 8" fill="none" stroke="#2aa3de" stroke-width="1"><rect x=".5" y="2" width="7" height="5.5"/><path d="M.5 2L4 5l3.5-3"/></svg>Enter Your Email</div>
<div class="abs signup"><svg width="16" height="14" viewBox="0 0 16 14" fill="#fff"><path d="M0 6L16 0 12 14 8 9 14 2 6 8z"/></svg>SIGN UP</div>

<div class="abs f-bottom">© 2015 TRNV Chartered Accountants. All rights reserved. &nbsp;| &nbsp;Privacy Policy &nbsp;| &nbsp;Site Map</div>
<div class="abs f-follow">Follow Us <i></i><i></i><i></i></div>

</body>
</html>
```